Web Button design and production

I need remote control like buttons (or your own design of buttons if I like it)
3x4 text buttons (normal, pressed, disabled)
3x1 empty button (normal, pressed, disabled)
3x6 buttons with glyph (normal, pressed, disabled)
3x288 with 24h time "00:00", "00:05", "00:10" (normal, pressed, disabled)
4 LED (red, green, orange, black)
I will upload the background image as soon as possible (black plastic)
See attached images
Q: Do the buttons have to be gray/black?
A: It should look like a high end remote control. It could be brushed aluminum as well, or something you come up with. But I guess black or dark grey would be best. The background will be picsharbor 40561739, but it's not available yet.
Q: Do I have to provide all buttons for the contest?
A: No! I only need one button (3 states) and a LED to decide. Only the winner will do the whole job.
Q: Is the Designer who wins the contest expected to complete all the extra buttons?
A: Yes, please.
Plastic

```html
<!DOCTYPE html>
<html lang="en">
<head>
<meta charset="utf-8">
<title>Remote Control Button Set</title>
<link rel="stylesheet" href="https://fonts.googleapis.com/css2?family=Quicksand:wght@300;400;500;600&display=swap">
<style>
  :root {
    --bg: #2c2c2e;
    --bg-light: #333336;
    --panel-line: #3d3d40;
    --panel-fill: #2f2f31;
    --btn-top: #46464a;
    --btn-bottom: #2f2f33;
    --btn-edge: #1a1a1c;
    --btn-pressed-top: #2a2a2d;
    --btn-pressed-bottom: #3a3a3e;
    --label: #77777b;
    --text-on: #bdbdc0;
    --text-pressed: #d6d6d9;
    --text-disabled: #5a5a5e;
    --link-dim: #8a8a8e;
    --link-bright: #f2f2f4;
    --led-green: #22d42e;
    --led-red: #e01818;
    --led-orange: #f0a010;
    --led-black: #0b0b0c;
  }
  * { box-sizing: border-box; margin: 0; padding: 0; }
  html, body { width: 1200px; height: 735px; overflow: hidden; }
  body {
    background: radial-gradient(ellipse at 50% 40%, var(--bg-light), var(--bg) 70%);
    font-family: "Quicksand", sans-serif;
    position: relative;
  }
  .panel {
    position: absolute; left: 111px; top: 89px; width: 983px; height: 496px;
    border: 2px solid var(--panel-line); border-radius: 10px;
    background: var(--panel-fill);
    box-shadow: inset 0 1px 0 rgba(255,255,255,0.03);
  }
  .state-label {
    position: absolute; top: 102px; width: 300px; margin-left: -150px;
    text-align: center; font-size: 29px; font-weight: 400; color: var(--label);
  }
  .btn {
    position: absolute; display: flex; align-items: center; justify-content: center;
    font-weight: 400; border-radius: 14px;
  }
  .btn--on {
    background: linear-gradient(var(--btn-top), var(--btn-bottom));
    border: 3px solid var(--btn-edge);
    box-shadow: inset 0 2px 0 rgba(255,255,255,0.12), 0 3px 4px rgba(0,0,0,0.4);
    color: var(--text-on);
  }
  .btn--pressed {
    background: linear-gradient(var(--btn-pressed-top), var(--btn-pressed-bottom));
    border: 3px solid #7a7a80;
    box-shadow: inset 0 4px 8px rgba(0,0,0,0.6), 0 0 0 2px var(--btn-edge);
    color: var(--text-pressed);
  }
  .btn--disabled {
    background: transparent;
    border: 3px solid #3a3a3d;
    box-shadow: inset 0 1px 0 rgba(255,255,255,0.04);
    color: var(--text-disabled);
  }
  .btn--text { top: 170px; height: 84px; width: 270px; font-size: 42px; }
  .btn--time { top: 339px; height: 89px; width: 135px; font-size: 40px; border-radius: 16px; }
  .text-link {
    position: absolute; top: 496px; font-size: 28px; font-weight: 600;
    text-decoration: underline; text-underline-offset: 5px;
  }
  .text-link--dim { left: 160px; color: var(--link-dim); }
  .text-link--bright { left: 334px; color: var(--link-bright); }
  .link-btn {
    position: absolute; top: 484px; width: 202px; height: 61px;
    display: flex; align-items: center; justify-content: center;
    font-size: 28px; font-weight: 600; border: 2px solid #1c1c1e;
  }
  .link-btn--dim { left: 627px; background: linear-gradient(#3c3c40, #343437); color: #a5a5a9;
    box-shadow: inset 0 1px 0 rgba(255,255,255,0.08); }
  .link-btn--active { left: 851px; background: #1f1f21; color: var(--link-bright);
    box-shadow: inset 0 2px 4px rgba(0,0,0,0.6); }
  .led {
    position: absolute; top: 632px; width: 44px; height: 44px; border-radius: 50%;
    border: 4px solid #1d1d1f;
    box-shadow: 0 1px 0 rgba(255,255,255,0.08);
  }
  .led--green { left: 430px; background: radial-gradient(circle at 45% 40%, #b8ffb0, var(--led-green) 45%, #0d7a14); }
  .led--red { left: 529px; background: radial-gradient(circle at 45% 40%, #ff9a9a, var(--led-red) 45%, #7a0808); }
  .led--orange { left: 627px; background: radial-gradient(circle at 45% 40%, #ffe08a, var(--led-orange) 45%, #8a5500); }
  .led--black { left: 723px; background: radial-gradient(circle at 50% 55%, #3a3a3c, var(--led-black) 55%); }
</style>
</head>
<body>
  <div class="panel"></div>

  <div class="state-label" style="left:275px">On</div>
  <div class="state-label" style="left:602px">Depressed</div>
  <div class="state-label" style="left:926px">Disabled</div>

  <div class="btn btn--on btn--text" style="left:140px">Text</div>
  <div class="btn btn--pressed btn--text" style="left:467px">Text</div>
  <div class="btn btn--disabled btn--text" style="left:791px">Text</div>

  <div class="btn btn--on btn--time" style="left:204px">17:25</div>
  <div class="btn btn--pressed btn--time" style="left:529px">17:25</div>
  <div class="btn btn--disabled btn--time" style="left:858px">17:25</div>

  <span class="text-link text-link--dim">Text Link</span>
  <span class="text-link text-link--bright">Text Link</span>

  <div class="link-btn link-btn--dim">Text Link</div>
  <div class="link-btn link-btn--active">Text Link</div>

  <div class="led led--green" aria-label="Green LED"></div>
  <div class="led led--red" aria-label="Red LED"></div>
  <div class="led led--orange" aria-label="Orange LED"></div>
  <div class="led led--black" aria-label="Black LED"></div>
</body>
</html>
```